Terra Daily and Current Affairs website

We intends to start up a new website which deals on New and Current Affairs.
Attention Designers,
We want a home page design for this project. Our business is based in the United States. Our goal is to become a well known brand.
The website would consist of a category for News, Business and Tech.
The theme should be beautiful and attention seeking. The website would take bulk of it's news from the US, and Europe.
Designers can get inspiration from already existing new websites such as HVZ, FQJ, DORNAKE.
All designs should be clean and easy to navigate.

```html
<!DOCTYPE html>
<html lang="en">
<head>
<meta charset="utf-8">
<title>Terra Daily</title>
<link rel="stylesheet" href="https://fonts.googleapis.com/css2?family=Montserrat:wght@400;500;600;700;800&family=Open+Sans:wght@400;600&display=swap">
<style>
:root{
  --ink:#111;
  --text:#222;
  --muted:#8a8a8a;
  --line:#e6e6e6;
  --topbar:#f4f4f4;
  --news:#a04fd0;
  --tech:#f5b400;
  --business:#1c8fe3;
  --pink:#ea2bbd;
  --green:#4bd61d;
  --hero-news:#f1c40f;
  --hero-tech:#e42bc8;
  --footer:#050505;
  --footer-text:#9a9a9a;
  --fb:#3b5998;--tw:#1da1f2;--ig:#9b6a4e;--yt:#e52d27;
}
*{box-sizing:border-box;margin:0;padding:0}
html,body{width:1200px;height:2752px;overflow:hidden;background:#fff}
body{font-family:"Open Sans",Arial,sans-serif;color:var(--text)}
.page{position:relative;width:1200px;height:2752px;overflow:hidden}
.abs{position:absolute}

/* top bar */
.topbar{top:0;left:0;width:1200px;height:31px;background:var(--topbar)}
.topbar .socials{position:absolute;left:210px;top:11px;display:flex;gap:8px}
.topbar .socials span{width:9px;height:9px;background:#222;display:block}
.topbar .links{position:absolute;right:210px;top:9px;display:flex;gap:18px;font:700 9px "Montserrat",sans-serif;color:#111}

/* header */
.masthead{top:31px;left:0;width:1200px;height:85px;border-bottom:1px solid var(--line)}
.burger{position:absolute;left:210px;top:40px;width:13px}
.burger i{display:block;height:2px;background:#111;margin-bottom:3px}
.brand{position:absolute;left:0;right:0;top:32px;text-align:center;font:600 18px "Montserrat",sans-serif;color:#111;letter-spacing:-.2px}
.search{position:absolute;left:976px;top:38px}
.mainnav{top:117px;left:0;width:1200px;height:46px;border-bottom:1px solid var(--line);display:flex;justify-content:center;gap:38px;padding-top:16px;font:700 9px "Montserrat",sans-serif;color:#111;letter-spacing:.3px}

/* hero */
.hero{top:165px;left:0;width:1200px;height:279px;display:flex}
.hero-card{position:relative;width:400px;height:279px;overflow:hidden}
.hero-card .photo{position:absolute;inset:0}
.hero-card .shade{position:absolute;inset:0;background:linear-gradient(180deg,rgba(0,0,0,0) 45%,rgba(0,0,0,.75) 100%)}
.hero-card .cap{position:absolute;left:16px;right:10px;bottom:14px;color:#fff}
.hero-card .tag{display:inline-block;font:700 7px "Montserrat",sans-serif;color:#fff;padding:3px 6px;margin-bottom:6px;text-transform:uppercase}
.hero-card h2{font:700 16px/20px "Montserrat",sans-serif;letter-spacing:-.4px;margin-bottom:6px}
.hero-card .by{font:600 8px "Montserrat",sans-serif}

/* section heading chip */
.chip-head{height:22px;border-bottom:2px solid currentColor;position:relative}
.chip-head .chip{position:absolute;left:0;top:0;height:20px;padding:0 12px;display:flex;align-items:center;font:700 8px "Montserrat",sans-serif;color:#fff;text-transform:uppercase;letter-spacing:.3px}
.chip-head .arrows{position:absolute;right:0;top:0;display:flex;gap:2px}
.chip-head .arrows span{width:16px;height:20px;background:currentColor;display:flex;align-items:center;justify-content:center}
.dark-head{height:22px;border-bottom:1px solid #ccc;position:relative}
.dark-head .chip{position:absolute;left:0;top:0;height:21px;padding:0 12px;display:flex;align-items:center;font:700 8px "Montserrat",sans-serif;color:#fff;background:#111;text-transform:uppercase}

/* article card */
.card .photo{width:246px;height:172px}
.card h3{font:700 12px/18px "Montserrat",sans-serif;letter-spacing:-.3px;color:var(--ink);margin-top:16px}
.card p{font:600 9.5px/16px "Open Sans",sans-serif;color:var(--muted);margin-top:6px}
.meta{display:flex;align-items:center;gap:10px;font:600 8.5px "Montserrat",sans-serif;color:#777;margin-top:12px}
.meta span{display:flex;align-items:center;gap:3px}
.meta svg{width:9px;height:9px}

.mini{display:flex;gap:14px;margin-top:14px}
.mini .thumb{width:105px;height:70px;flex:none}
.mini h4{font:700 9.5px/14px "Montserrat",sans-serif;letter-spacing:-.2px;color:var(--ink)}
.mini .date{font:400 8px "Open Sans",sans-serif;color:var(--muted);margin-top:8px}

.slide-card{width:180px}
.slide-card .photo{width:180px;height:112px}
.slide-card h4{font:700 10px/15px "Montserrat",sans-serif;letter-spacing:-.2px;color:var(--ink);margin-top:13px}
.slide-card .meta{margin-top:10px;gap:8px;font-size:7.5px}

/* sidebar */
.featured{width:246px;height:272px;position:relative;overflow:hidden}
.featured .txt{position:absolute;left:18px;right:18px;top:86px;text-align:center;color:#fff}
.featured .tag{display:inline-block;background:var(--pink);font:700 7px "Montserrat",sans-serif;padding:3px 6px;margin-bottom:6px}
.featured h3{font:700 12px/16px "Montserrat",sans-serif;letter-spacing:-.2px}
.featured .by{font:600 7.5px "Montserrat",sans-serif;margin-top:8px}
.featured .dots{position:absolute;bottom:24px;left:0;right:0;display:flex;justify-content:center;gap:5px}
.featured .dots i{width:6px;height:6px;border-radius:50%;background:#ddd;display:block}

.follow-row{height:31px;border:1px solid var(--line);display:flex;align-items:center;margin-bottom:4px;font:700 7.5px "Montserrat",sans-serif;color:#111;text-transform:uppercase}
.follow-row .ico{width:31px;height:31px;margin:-1px 14px 0 -1px;display:flex;align-items:center;justify-content:center}
.follow-row .ico i{width:9px;height:9px;background:#fff;display:block}
.follow-row .act{margin-left:auto;margin-right:12px}

.recent{display:flex;gap:12px;margin-bottom:14px}
.recent .thumb{width:96px;height:60px;flex:none}
.recent .cat{font:700 7px "Montserrat",sans-serif;text-transform:uppercase}
.recent h4{font:700 9px/13px "Montserrat",sans-serif;color:var(--ink);margin-top:3px}
.recent .date{font:400 7.5px "Open Sans",sans-serif;color:var(--muted);margin-top:4px}

.ad{width:246px;height:212px;position:relative;overflow:hidden}
.ad .org{position:absolute;left:14px;top:12px;font:700 9px/11px "Montserrat",sans-serif;color:#fff;width:70px}
.ad .badge{position:absolute;right:12px;top:8px;width:38px;height:32px;background:#fff;border-radius:3px}
.ad .band{position:absolute;left:0;right:0;bottom:0;height:70px;background:#1f5aa6;color:#fff;padding:12px 14px}
.ad .band b{font:700 15px "Open Sans",sans-serif;display:block}
.ad .band small{font:600 9px "Open Sans",sans-serif;display:block;margin-top:5px}
.ad .more{position:absolute;left:96px;bottom:-1px;background:#fff;color:#1f5aa6;font:700 6px "Montserrat",sans-serif;padding:2px 6px}
.ad-note{font:400 8px "Open Sans",sans-serif;color:#555;text-align:center}

/* footer */
.footer{top:2382px;left:0;width:1200px;height:370px;background:var(--footer);color:var(--footer-text)}
.fcol{position:absolute;top:44px;width:180px}
.fhead{height:20px;border-bottom:1px solid #333;position:relative;margin-bottom:18px}
.fhead span{position:absolute;left:0;top:0;height:20px;background:#1c1c1c;color:#fff;font:700 7.5px "Montserrat",sans-serif;padding:0 10px;display:flex;align-items:center;text-transform:uppercase}
.fcol p{font:400 9px/16px "Open Sans",sans-serif}
.fsocial{display:flex;gap:4px}
.fsocial span{width:17px;height:17px;border:1px solid #555;display:block}
.pop{margin-bottom:14px}
.pop .cat{font:700 7px "Montserrat",sans-serif;text-transform:uppercase}
.pop p{font:400 8.5px/13px "Open Sans",sans-serif;margin-top:2px}
.pop .date{font:700 8px "Montserrat",sans-serif;color:#fff;margin-top:4px}
.feed{display:grid;grid-template-columns:repeat(3,57px);gap:4px}
.feed div{height:57px}
.catlist div{display:flex;justify-content:space-between;font:600 7.5px "Montserrat",sans-serif;text-transform:uppercase;padding:9px 0;border-bottom:1px solid #262626}
.fbottom{position:absolute;left:211px;right:211px;top:303px;border-top:1px solid #262626;padding-top:28px;display:flex;justify-content:space-between;font:400 8px "Open Sans",sans-serif}
.fbottom nav{display:flex;gap:18px}
</style>
</head>
<body>
<svg width="0" height="0" style="position:absolute">
  <symbol id="i-eye" viewBox="0 0 10 10"><path d="M0.5 5C2 2.5 8 2.5 9.5 5C8 7.5 2 7.5 0.5 5Z" fill="none" stroke="#888" stroke-width="1"/><circle cx="5" cy="5" r="1.4" fill="#888"/></symbol>
  <symbol id="i-chat" viewBox="0 0 10 10"><path d="M1 1.5H9V7H4L2 9V7H1Z" fill="none" stroke="#888" stroke-width="1"/></symbol>
  <symbol id="i-like" viewBox="0 0 10 10"><path d="M1 4.5H3V9H1ZM3.5 4.5L5.5 1C6.5 1 6.8 1.8 6.5 3.5H9L8.3 9H3.5Z" fill="none" stroke="#888" stroke-width="1"/></symbol>
  <symbol id="i-left" viewBox="0 0 10 10"><path d="M6 2L3 5L6 8" fill="none" stroke="#fff" stroke-width="1.5"/></symbol>
  <symbol id="i-right" viewBox="0 0 10 10"><path d="M4 2L7 5L4 8" fill="none" stroke="#fff" stroke-width="1.5"/></symbol>
</svg>

<div class="page">

  <div class="abs topbar">
    <div class="socials"><span></span><span></span><span></span></div>
    <div class="links"><span>Authors</span><span>Contact Us</span><span>More</span></div>
  </div>

  <header class="abs masthead">
    <div class="burger"><i></i><i></i><i></i></div>
    <div class="brand">Terra Daily</div>
    <svg class="search" width="12" height="12" viewBox="0 0 12 12"><circle cx="5" cy="5" r="3.6" fill="none" stroke="#111" stroke-width="1.6"/><path d="M7.6 7.6L11 11" stroke="#111" stroke-width="1.8"/></svg>
  </header>

  <nav class="abs mainnav"><span>HOME</span><span>ABOUT</span><span>FEATURES</span><span>NEWS</span><span>TECHNOLOGY</span><span>BUSINESS</span></nav>

  <section class="abs hero">
    <article class="hero-card">
      <div class="photo" role="img" aria-label="Protesters in a street with tear gas smoke" style="background:linear-gradient(160deg,#6b6b6b 0%,#bdbdbd 40%,#e8e8e8 55%,#5a5550 100%)"></div>
      <div class="shade"></div>
      <div class="cap"><span class="tag" style="background:var(--hero-news)">News</span>
        <h2>Venezuelans to pay tribute to 22 dead in weeks of violent protests</h2>
        <div class="by">Marco Delvani · April 22, 2017</div></div>
    </article>
    <article class="hero-card">
      <div class="photo" role="img" aria-label="Smartphone held up against a blurred city street" style="background:radial-gradient(circle at 45% 35%,#dfe6ea 0%,#8fa0a8 30%,#3d4a44 60%,#b8a06a 100%)"></div>
      <div class="shade"></div>
      <div class="cap"><span class="tag" style="background:var(--hero-tech)">Technology</span>
        <h2>Beijing's internet regulators are turning up the heat on Orchard</h2>
        <div class="by">Marco Delvani · April 22, 2017</div></div>
    </article>
    <article class="hero-card">
      <div class="photo" role="img" aria-label="People beside an aircraft on a runway at night" style="background:linear-gradient(180deg,#0b0f1a 0%,#1a2233 50%,#4a4f58 70%,#1b1d22 100%)"></div>
      <div class="shade"></div>
      <div class="cap"><span class="tag" style="background:var(--business)">Business</span>
        <h2>Friendlink to beam internet from helicopters, New aged deal</h2>
        <div class="by">Marco Delvani · April 22, 2017</div></div>
    </article>
  </section>

  <section class="abs" style="top:475px;left:211px;width:246px">
    <div class="chip-head" style="color:var(--news)"><span class="chip" style="background:var(--news)">News</span></div>
    <div class="card" style="margin-top:17px">
      <div class="photo" role="img" aria-label="Politician speaking in front of flags" style="background:linear-gradient(135deg,#1d2233 0%,#4a4e63 50%,#8a3030 100%)"></div>
      <h3>Seamlessly Create Robust Paradigms Whereas Covalent</h3>
      <p>Efficiently reintermediate clicks-and-mortar web-readiness and holistic leadership skills. Synergistically restore strategic technology and emerging e-services. Compellingly maintain top-line</p>
      <div class="meta"><span>August 23, 2016</span><span><svg><use href="#i-eye"/></svg>347</span><span><svg><use href="#i-chat"/></svg>15</span><span><svg><use href="#i-like"/></svg>48</span></div>
    </div>
    <div class="mini"><div class="thumb" role="img" aria-label="Leaders at a podium with flags" style="background:linear-gradient(135deg,#c83a3a,#e6e6ef 50%,#2a3a8a)"></div><div><h4>Interactively strategize vertical architectures whereas transparent convergence...</h4><div class="date">July 12, 2016</div></div></div>
    <div class="mini"><div class="thumb" role="img" aria-label="Official speaking at a press event" style="background:linear-gradient(135deg,#1b2a5a,#3a4e8c 60%,#a33)"></div><div><h4>Monotonectally negotiate distinctive strategic theme areas and standardized...</h4><div class="date">July 12, 2016</div></div></div>
  </section>

  <section class="abs" style="top:475px;left:477px;width:246px">
    <div class="chip-head" style="color:var(--tech)"><span class="chip" style="background:var(--tech)">Technology</span></div>
    <div class="card" style="margin-top:17px">
      <div class="photo" role="img" aria-label="Smartwatch on a dark surface" style="background:radial-gradient(circle at 50% 50%,#6a6a6a 0%,#2a2a2a 50%,#0d0d0d 100%)"></div>
      <h3>Seamlessly Create Robust Paradigms Whereas Covalent</h3>
      <p>Efficiently reintermediate clicks-and-mortar web-readiness and holistic leadership skills. Synergistically restore strategic technology and emerging e-services. Compellingly maintain top-line</p>
      <div class="meta"><span>August 23, 2016</span><span><svg><use href="#i-eye"/></svg>347</span><span><svg><use href="#i-chat"/></svg>15</span><span><svg><use href="#i-like"/></svg>48</span></div>
    </div>
    <div class="mini"><div class="thumb" role="img" aria-label="Hooded figure at a computer" style="background:linear-gradient(135deg,#0e0e10,#3a3d44)"></div><div><h4>Rapidiously productize fully researched technologies whereas backend content...</h4><div class="date">July 12, 2016</div></div></div>
    <div class="mini"><div class="thumb" role="img" aria-label="Hand holding a smartphone outdoors" style="background:linear-gradient(135deg,#8aa06a,#d8d2c0 50%,#7a6a4a)"></div><div><h4>Energistically optimize accurate information with intuitive initiatives...</h4><div class="date">July 12, 2016</div></div></div>
  </section>

  <section class="abs" style="top:475px;left:743px;width:246px">
    <div class="chip-head" style="color:var(--business)"><span class="chip" style="background:var(--business)">Business</span></div>
    <div class="card" style="margin-top:17px">
      <div class="photo" role="img" aria-label="Container port with cranes under a blue sky" style="background:linear-gradient(180deg,#9cc8ea 0%,#d6e6f2 40%,#3a7fb0 60%,#b84a3a 80%,#2b5f7a 100%)"></div>
      <h3>Seamlessly Create Robust Paradigms Whereas Covalent</h3>
      <p>Efficiently reintermediate clicks-and-mortar web-readiness and holistic leadership skills. Synergistically restore strategic technology and emerging e-services. Compellingly maintain top-line</p>
      <div class="meta"><span>August 23, 2016</span><span><svg><use href="#i-eye"/></svg>347</span><span><svg><use href="#i-chat"/></svg>15</span><span><svg><use href="#i-like"/></svg>48</span></div>
    </div>
    <div class="mini"><div class="thumb" role="img" aria-label="Conference hall with audience" style="background:linear-gradient(135deg,#3a2a1a,#8a6a3a 50%,#2a1e18)"></div><div><h4>Rapidiously productize fully researched technologies whereas backend content...</h4><div class="date">July 12, 2016</div></div></div>
    <div class="mini"><div class="thumb" role="img" aria-label="Business leaders shaking hands" style="background:linear-gradient(135deg,#2a2a2e,#7a6a5a 50%,#1e1e22)"></div><div><h4>Energistically optimize accurate information with intuitive initiatives...</h4><div class="date">July 12, 2016</div></div></div>
  </section>

  <section class="abs" style="top:1028px;left:211px;width:380px">
    <div class="chip-head" style="color:var(--pink)"><span class="chip" style="background:var(--pink)">Business</span><span class="arrows"><span><svg width="10" height="10"><use href="#i-left"/></svg></span><span><svg width="10" height="10"><use href="#i-right"/></svg></span></span></div>
    <div style="display:flex;gap:20px;margin-top:18px">
      <div class="slide-card"><div class="photo" role="img" aria-label="Colleagues meeting at an office table" style="background:linear-gradient(135deg,#dfe6ee,#8ea3b8 60%,#404a58)"></div><h4>The Big Oxmox Advised Her Not to Do So, Because There Were</h4><div class="meta"><span>August 23, 2016</span><span><svg><use href="#i-eye"/></svg>347</span><span><svg><use href="#i-chat"/></svg>15</span><span><svg><use href="#i-like"/></svg>48</span></div></div>
      <div class="slide-card"><div class="photo" role="img" aria-label="Hands reviewing documents on a desk" style="background:linear-gradient(135deg,#f0f0f0,#b8b8b8 55%,#3c3c3c)"></div><h4>The Big Oxmox Advised Her Not to Do So, Because There Were</h4><div class="meta"><span>August 23, 2016</span><span><svg><use href="#i-eye"/></svg>347</span><span><svg><use href="#i-chat"/></svg>15</span><span><svg><use href="#i-like"/></svg>48</span></div></div>
    </div>
  </section>

  <section class="abs" style="top:1028px;left:609px;width:380px">
    <div class="chip-head" style="color:var(--green)"><span class="chip" style="background:var(--green)">Technology</span><span class="arrows"><span><svg width="10" height="10"><use href="#i-left"/></svg></span><span><svg width="10" height="10"><use href="#i-right"/></svg></span></span></div>
    <div style="display:flex;gap:20px;margin-top:18px">
      <div class="slide-card"><div class="photo" role="img" aria-label="Person touching a digital world map display" style="background:linear-gradient(135deg,#5a7a8a,#9cb4be 50%,#2e4452)"></div><h4>The Big Oxmox Advised Her Not to Do So, Because There Were</h4><div class="meta"><span>August 23, 2016</span><span><svg><use href="#i-eye"/></svg>347</span><span><svg><use href="#i-chat"/></svg>15</span><span><svg><use href="#i-like"/></svg>48</span></div></div>
      <div class="slide-card"><div class="photo" role="img" aria-label="Drone flying at sunset" style="background:linear-gradient(180deg,#c9962e 0%,#e2b84a 50%,#6a4a1a 100%)"></div><h4>The Big Oxmox Advised Her Not to Do So, Because There Were</h4><div class="meta"><span>August 23, 2016</span><span><svg><use href="#i-eye"/></svg>347</span><span><svg><use href="#i-chat"/></svg>15</span><span><svg><use href="#i-like"/></svg>48</span></div></div>
    </div>
  </section>

  <section class="abs" style="top:1284px;left:211px;width:512px;display:grid;grid-template-columns:246px 246px;grid-auto-rows:307px;column-gap:20px;row-gap:40px">
    <div class="card"><div class="photo" role="img" aria-label="Tall office tower against the sky" style="background:linear-gradient(135deg,#e6edf3,#8a9aa8 50%,#3a4652)"></div><h3>Seamlessly Create Robust Paradigms Whereas Covalent</h3><p>Efficiently reintermediate clicks-and-mortar ek-readiness and holistic leadership skills. Synergistically restore strategic technology and emerging e-services. mpellingly maintain top-line e-markets.</p><div class="meta"><span>August 23, 2016</span><span><svg><use href="#i-eye"/></svg>347</span><span><svg><use href="#i-chat"/></svg>15</span><span><svg><use href="#i-like"/></svg>48</span></div></div>
    <div class="card"><div class="photo" role="img" aria-label="Iceberg floating in dark water seen from above" style="background:radial-gradient(ellipse at 50% 50%,#e8eef2 0%,#8fa6b2 25%,#15222c 55%,#0a1218 100%)"></div><h3>Seamlessly Create Robust Paradigms Whereas Covalent</h3><p>Efficiently reintermediate clicks-and-mortar ek-readiness and holistic leadership skills. Synergistically restore strategic technology and emerging e-services. Mpellingly maintain top-line e-markets.</p><div class="meta"><span>August 23, 2016</span><span><svg><use href="#i-eye"/></svg>347</span><span><svg><use href="#i-chat"/></svg>15</span><span><svg><use href="#i-like"/></svg>48</span></div></div>
    <div class="card"><div class="photo" role="img" aria-label="Pair of sneakers on a dark background" style="background:radial-gradient(circle at 55% 50%,#9a9a9a 0%,#4a4a4a 35%,#0e0e0e 75%)"></div><h3>Seamlessly Create Robust Paradigms Whereas Covalent</h3><p>Efficiently reintermediate clicks-and-mortar web-readiness and holistic leadership skills. Synergistically restore strategic technology and emerging e-services. Compellingly maintain top-line</p><div class="meta"><span>August 23, 2016</span><span><svg><use href="#i-eye"/></svg>347</span><span><svg><use href="#i-chat"/></svg>15</span><span><svg><use href="#i-like"/></svg>48</span></div></div>
    <div class="card"><div class="photo" role="img" aria-label="Compact camera on a black background" style="background:radial-gradient(circle at 50% 55%,#5a5a5a 0%,#222 40%,#050505 80%)"></div><h3>Seamlessly Create Robust Paradigms Whereas Covalent</h3><p>Efficiently reintermediate clicks-and-mortar ek-readiness and holistic leadership skills. Synergistically restore strategic technology and emerging e-services. Compellingly maintain top-line e-markets.</p><div class="meta"><span>August 23, 2016</span><span><svg><use href="#i-eye"/></svg>347</span><span><svg><use href="#i-chat"/></svg>15</span><span><svg><use href="#i-like"/></svg>48</span></div></div>
    <div class="card"><div class="photo" role="img" aria-label="Tall office tower against the sky" style="background:linear-gradient(135deg,#e6edf3,#8a9aa8 50%,#3a4652)"></div><h3>Seamlessly Create Robust Paradigms Whereas Covalent</h3><p>Efficiently reintermediate clicks-and-mortar ek-readiness and holistic leadership skills. Synergistically restore strategic technology and emerging e-services. mpellingly maintain top-line e-markets.</p><div class="meta"><span>August 23, 2016</span><span><svg><use href="#i-eye"/></svg>347</span><span><svg><use href="#i-chat"/></svg>15</span><span><svg><use href="#i-like"/></svg>48</span></div></div>
    <div class="card"><div class="photo" role="img" aria-label="Iceberg floating in dark water seen from above" style="background:radial-gradient(ellipse at 50% 50%,#e8eef2 0%,#8fa6b2 25%,#15222c 55%,#0a1218 100%)"></div><h3>Seamlessly Create Robust Paradigms Whereas Covalent</h3><p>Efficiently reintermediate clicks-and-mortar ek-readiness and holistic leadership skills. Synergistically restore strategic technology and emerging e-services. Mpellingly maintain top-line e-markets.</p><div class="meta"><span>August 23, 2016</span><span><svg><use href="#i-eye"/></svg>347</span><span><svg><use href="#i-chat"/></svg>15</span><span><svg><use href="#i-like"/></svg>48</span></div></div>
  </section>

  <aside class="abs" style="top:1284px;left:743px;width:246px">
    <div class="featured">
      <div role="img" aria-label="Dark office interior" style="position:absolute;inset:0;background:linear-gradient(160deg,#4a4a4a 0%,#2a2a2a 50%,#3c3c3c 100%)"></div>
      <div class="txt"><span class="tag">Business</span><h3>Revolutionize Superior Deliverables Without Market Positioning Convergence</h3><div class="by">Marco Delvani · Mar 12, 2017</div></div>
      <div class="dots"><i></i><i></i><i></i><i></i></div>
    </div>

    <div class="dark-head" style="margin-top:40px"><span class="chip">Follow Us</span></div>
    <div style="margin-top:14px">
      <div class="follow-row"><span class="ico" style="background:var(--fb)"><i></i></span>Friendlink<span class="act">Like</span></div>
      <div class="follow-row"><span class="ico" style="background:var(--tw)"><i></i></span>Chirpline<span class="act">Follow</span></div>
      <div class="follow-row"><span class="ico" style="background:var(--ig)"><i></i></span>Pictora<span class="act">Follow</span></div>
      <div class="follow-row"><span class="ico" style="background:var(--yt)"><i></i></span>Vidstream<span class="act">Subscribe</span></div>
    </div>

    <div class="dark-head" style="margin-top:30px"><span class="chip">Recent Post</span></div>
    <div style="margin-top:16px">
      <div class="recent"><div class="thumb" role="img" aria-label="Busy street scene" style="background:linear-gradient(135deg,#3a2a1e,#9a7a4a)"></div><div><div class="cat" style="color:var(--green)">News</div><h4>Buzz Would Certainly Come Round With the Doctor</h4><div class="date">July 12, 2016</div></div></div>
      <div class="recent"><div class="thumb" role="img" aria-label="Hand holding a smartphone outdoors" style="background:linear-gradient(135deg,#8aa06a,#d8d2c0 50%,#7a6a4a)"></div><div><div class="cat" style="color:var(--tech)">Technology</div><h4>That's When I'll Make the Big Change</h4><div class="date">July 12, 2016</div></div></div>
      <div class="recent"><div class="thumb" role="img" aria-label="Hands reviewing documents on a desk" style="background:linear-gradient(135deg,#f0f0f0,#b8b8b8 55%,#3c3c3c)"></div><div><div class="cat" style="color:var(--pink)">Business</div><h4>Doing Business Like Takes Much More Effort</h4><div class="date">July 12, 2016</div></div></div>
    </div>

    <div class="ad" style="margin-top:6px">
      <div role="img" aria-label="Smiling older man in a suit" style="position:absolute;inset:0;background:linear-gradient(135deg,#b8c8d6 0%,#dfe6ea 45%,#8a6e5a 70%,#3a4a6a 100%)"></div>
      <div class="org">Grant a Dream</div>
      <div class="badge"></div>
      <div class="band"><b>We are grateful for you.</b><small>Celebrate World Dream Day®, 29 April</small></div>
      <span class="more">LEARN MORE</span>
    </div>
    <div class="ad-note" style="margin-top:4px">Advertisement</div>
  </aside>

  <footer class="abs footer">
    <div class="fcol" style="left:211px">
      <div class="fhead"><span>About Us</span></div>
      <p>The bedding was hardly able to cover it and seemed ready to slide off any moment. His many legs, pitifully thin compared with the size of the rest of him, waved about helplessly as he looked.</p>
      <div class="fhead" style="margin-top:22px"><span>Social Media</span></div>
      <div class="fsocial"><span></span><span></span><span></span><span></span><span></span><span></span></div>
    </div>
    <div class="fcol" style="left:411px">
      <div class="fhead"><span>Popular Posts</span></div>
      <div class="pop"><div class="cat" style="color:var(--green)">Politics</div><p>Doing business like this takes much more effort than doing...</p><div class="date">July 12, 2016</div></div>
      <div class="pop"><div class="cat" style="color:var(--tech)">Technology</div><p>The most train went at seven. If he were to catch that he would...</p><div class="date">July 12, 2016</div></div>
      <div class="pop"><div class="cat" style="color:var(--pink)">Business</div><p>The office assistant was the boss's man, spineless, and with understanding...</p><div class="date">July 12, 2016</div></div>
    </div>
    <div class="fcol" style="left:611px">
      <div class="fhead"><span>Pictora Feed</span></div>
      <div class="feed">
        <div role="img" aria-label="Black and white portrait photo" style="background:linear-gradient(135deg,#ddd,#555)"></div>
        <div role="img" aria-label="Black and white street photo" style="background:linear-gradient(135deg,#888,#222)"></div>
        <div role="img" aria-label="Black and white portrait photo" style="background:linear-gradient(135deg,#aaa,#333)"></div>
        <div role="img" aria-label="Black and white portrait photo" style="background:linear-gradient(135deg,#eee,#666)"></div>
        <div role="img" aria-label="Black and white crowd photo" style="background:linear-gradient(135deg,#777,#1a1a1a)"></div>
        <div role="img" aria-label="Black and white city photo" style="background:linear-gradient(135deg,#999,#2a2a2a)"></div>
      </div>
      <p style="margin-top:12px;color:#fff;font-size:8px">View More...</p>
    </div>
    <div class="fcol" style="left:809px">
      <div class="fhead"><span>Categories</span></div>
      <div class="catlist">
        <div><span>Culture</span><span>13</span></div>
        <div><span>Business</span><span>13</span></div>
        <div><span>Food</span><span>22</span></div>
        <div><span>Politics</span><span>13</span></div>
        <div><span>Magazine</span><span>14</span></div>
        <div><span>Music</span><span>13</span></div>
        <div><span>Technology</span><span>13</span></div>
      </div>
    </div>
    <div class="fbottom"><span>Copyrights 2017. All rights reserved.</span><nav><span>Home</span><span>About</span><span>Authors</span><span>Contact</span></nav></div>
  </footer>

</div>
</body>
</html>
```